Luxury Skincare Product Box Packaging Design

Vorabelle is a range of skincare products that help protect, nourish, and strengthen even the most sensitive skin, ensuring it is healthy, glowing, calm, and soft. Skincare practices support skin to enhance its appearance and relieve skin conditions. Your skin reflects your health. It is your body canvas and is an asset. The products contain naturally derived ingredients, aromatherapy oils, sustainable and ethical ingredients, organic ingredients where possible, natural preservatives and Australian oils, fruits, and extracts.

Vorabelle
Tagline is "Where Calm Finds Bloom"

Our products do not contain sulphates, parabens, phthalates, petrochemicals, synthetic colours, nor synthetic fragrances.

Everything about the Vorabelle Skincare name is creative and communicates luxury. Vorabelle from your first glance of the name, you will know that this is a company with excellent products.

By keeping it simple, unique, and elegant is often associated with high quality and is a way to establish trust. Vorabelle is a product that is “pure” and natural, so Vorabelle packaging would look simple, elegant, and clean.

I have uploaded the actual logo design and individual labels for the current skincare range I currently with the ingredients included so you can get an understanding of what I like. I have also added samples of package designs I quite like to assist with your designs.

Each Product box packaging sizes are as follows:

Product One - Exfoliating Herbs: 110mm (H) x 33mm Diameter
Product Two - Probiotic Lotion: 138mm (H) x 33mm Diameter
Product Three - Vitamin A Serum: 120mm (H) x 30mm Diameter
Updates

The Measurements are as follows: Product One: 110mm (H) x 33mm Diameter Product Two: 138mm (H) x 33mm Diameter Product Three: 120mm (H) x 30mm Diameter

Target Market(s)

Women

Requirements
Must have
• Logo, Product Name and ingredients and if you can barcode on the packaging that is the box design I am after
Nice to have
• samples of designs I like but open to suggestions

```html
<!DOCTYPE html>
<html lang="en">
<head>
<meta charset="utf-8">
<title>Vorabelle – Gentle Exfoliating Herbs Box Dieline</title>
<link href="https://fonts.googleapis.com/css2?family=Lato:wght@300;400;700&display=swap" rel="stylesheet">
<style>
  :root {
    --canvas: #ebebeb;
    --stock: #ffffff;
    --cut: #2b2b2b;
    --fold: #e9779a;
    --rose-light: #e2a98c;
    --rose-mid: #c4917a;
    --rose-dark: #9a6b51;
    --band-front: #b48468;
    --band-alt: #d6a083;
    --text-light: #ffffff;
    --text-ink: #1e1e1e;
    --bloom-green: #4f8f3a;
    --bloom-white: #f4f1ea;
  }
  * { margin: 0; padding: 0; box-sizing: border-box; }
  html, body { width: 1200px; height: 800px; overflow: hidden; background: var(--canvas); }
  .dieline { position: relative; width: 1200px; height: 800px; font-family: "Lato", sans-serif; }
  .dieline-shapes { position: absolute; inset: 0; }

  .panel-text { position: absolute; color: var(--text-light); }

  .side-copy {
    left: 315px; top: 278px; width: 124px;
    font-size: 9.3px; line-height: 11.25px; font-weight: 400;
  }
  .side-copy p + p { margin-top: 11px; }
  .side-copy strong { font-weight: 700; }

  .product-name {
    position: absolute; width: 147px; text-align: center;
    font-size: 9.4px; line-height: 12.4px; letter-spacing: 0.6px; color: var(--text-light);
  }
  .product-name.front { left: 445px; top: 528px; }
  .product-name.alt { left: 740px; top: 531px; }
  .product-name.lid { left: 445px; top: 172px; transform: rotate(180deg); }

  .brand-name {
    position: absolute; writing-mode: vertical-rl;
    font-family: "Lato", sans-serif; font-weight: 300;
    font-size: 30px; letter-spacing: 3px; color: var(--rose-mid);
  }
  .tagline {
    position: absolute; writing-mode: vertical-rl;
    font-size: 6.2px; letter-spacing: 3.1px; color: var(--text-ink);
  }
  .brand-name.front { left: 505px; top: 350px; }
  .tagline.front { left: 494px; top: 385px; }
  .brand-name.alt { left: 800px; top: 350px; }
  .tagline.alt { left: 789px; top: 385px; }

  .bloom {
    position: absolute; width: 73px; height: 86px;
    background: radial-gradient(circle at 58% 40%, var(--bloom-white) 0 34%, var(--bloom-green) 62%, rgba(79,143,58,0) 78%);
  }
  .bloom.front { left: 519px; top: 241px; }
  .bloom.alt { left: 814px; top: 241px; }

  .skin-types {
    left: 592px; top: 265px; width: 148px; text-align: center;
    font-size: 5.6px; line-height: 8.4px; font-weight: 400;
  }
  .badge-label {
    position: absolute; width: 34px; text-align: center;
    font-size: 4.4px; line-height: 5.4px; font-weight: 700; color: var(--text-light);
  }
  .care-note {
    left: 619px; top: 459px; width: 97px; height: 38px;
    border: 1px solid var(--text-light);
    font-size: 4.7px; line-height: 6.8px; font-weight: 700; text-align: center;
    padding-top: 4px;
  }
  .web-address {
    left: 592px; top: 539px; width: 148px; text-align: center;
    font-size: 6.2px; font-weight: 700; letter-spacing: 0.4px;
  }
</style>
</head>
<body>
<main class="dieline">
  <svg class="dieline-shapes" width="1200" height="800" viewBox="0 0 1200 800" aria-hidden="true">
    <defs>
      <linearGradient id="rose-panel" x1="0" y1="0" x2="1" y2="1">
        <stop offset="0" stop-color="#e2aa8d"/>
        <stop offset="1" stop-color="#986a50"/>
      </linearGradient>
      <linearGradient id="rose-lid" x1="0" y1="0" x2="1" y2="1">
        <stop offset="0" stop-color="#e5a98c"/>
        <stop offset="1" stop-color="#c4937a"/>
      </linearGradient>
      <linearGradient id="rose-base" x1="0" y1="0" x2="1" y2="1">
        <stop offset="0" stop-color="#d29c80"/>
        <stop offset="1" stop-color="#f0b497"/>
      </linearGradient>
    </defs>

    <g class="dust-flaps" fill="var(--stock)" stroke="var(--cut)" stroke-width="0.8">
      <polygon points="299.5,240 299.5,230.6 305,223 315,177 445,177 445,240"/>
      <polygon points="592,240 592,177 723,177 733,223 739,230.6 739,240"/>
      <polygon points="299.5,563 444,563 444,571 438,579 428.6,624 299.5,624"/>
      <polygon points="593,563 740,563 740,624 609,624 599.5,579 593,571"/>
      <polygon points="887,240 918,257 918,544 887,561"/>
    </g>

    <g class="tuck-lid" stroke="var(--cut)" stroke-width="0.8">
      <path d="M447,104 V78 Q447,67 458,67 H580 Q591,67 591,78 V104 Z" fill="url(#rose-lid)"/>
      <path d="M445,240 V103.6 H450 L454,107.5 H575 L579,103.6 H592 V240 Z" fill="url(#rose-lid)"/>
    </g>
    <g class="tuck-base" stroke="var(--cut)" stroke-width="0.8">
      <path d="M741,698 V724 Q741,735 752,735 H874 Q885,735 885,724 V698 Z" fill="url(#rose-base)"/>
      <path d="M740,563 V698 H744 L748,694 H869 L873,698 H887 V563 Z" fill="url(#rose-base)"/>
    </g>

    <g class="body-panels" stroke="var(--cut)" stroke-width="0.8">
      <rect class="side-panel" x="299.5" y="240" width="145.5" height="323" fill="url(#rose-panel)"/>
      <rect class="front-panel" x="445" y="240" width="147" height="321" fill="var(--stock)"/>
      <rect class="front-band" x="445" y="523" width="147" height="38" fill="var(--band-front)" stroke="none"/>
      <rect class="back-panel" x="592" y="240" width="148" height="323" fill="url(#rose-panel)"/>
      <rect class="alt-front-panel" x="740" y="240" width="147" height="323" fill="var(--stock)"/>
      <rect class="alt-front-band" x="740" y="523" width="147" height="40" fill="var(--band-alt)" stroke="none"/>
    </g>

    <g class="fold-lines" fill="none" stroke="var(--fold)" stroke-width="0.9" stroke-dasharray="5 3">
      <line x1="299.5" y1="240" x2="887" y2="240"/>
      <line x1="299.5" y1="563" x2="887" y2="563"/>
      <line x1="445" y1="240" x2="445" y2="563"/>
      <line x1="592" y1="240" x2="592" y2="563"/>
      <line x1="740" y1="240" x2="740" y2="563"/>
      <line x1="887" y1="240" x2="887" y2="563"/>
      <line x1="454" y1="106" x2="575" y2="106"/>
      <line x1="748" y1="696" x2="869" y2="696"/>
    </g>

    <g class="claim-icons" fill="none" stroke="var(--text-light)" stroke-width="0.9">
      <circle cx="636" cy="350" r="8.5"/>
      <path d="M670,344 a4.2,4.2 0 0 1 0,0 M670,359 l-9,-9 a5,5 0 0 1 9,-6 a5,5 0 0 1 9,6 z"/>
      <circle cx="701" cy="350" r="8.5"/>
      <path d="M646,401 l4,-7 4,7 M647,397 h-3 l5,-9 M656,392 l3,5 h-5 M646,403 h8 M652,388 l2,0"/>
      <rect x="676" y="391" width="14" height="12" rx="2"/>
      <line x1="676" y1="391" x2="690" y2="387"/>
      <text x="683" y="401" fill="var(--text-light)" stroke="none" font-family="Lato, sans-serif" font-size="5.5" text-anchor="middle">6 M</text>
    </g>
  </svg>

  <div class="product-name lid">Gentle<br>Exfoliating Herbs</div>

  <section class="panel-text side-copy">
    <p><strong>Directions:</strong> Mix a small amount with your favourite cleanser. Massage into your face for approximately one minute before removing with water or a face cloth. Use twice weekly.</p>
    <p><strong>INGREDIENTS:</strong> ORYZA SATIVA (RICE) POWDER*, ROSA GALLICA (ROSE PETALS)*, JASMINUM OFFICINALE (JASMINE) FLOWER, MATRICARIA RECUTITA (CHAMOMILE FLOWERS)*, CAMELLIA SINENSIS LEAF (GREEN TEA), LUFFA CYLINDRICA FRUIT POWDER, CALENDULA OFFICINALIS (MARIGOLD FLOWERS) <strong>*ORGANIC INGREDIENTS</strong></p>
  </section>

  <div class="bloom front" role="img" aria-label="Photograph of a white jasmine flower with green leaves"></div>
  <div class="brand-name front">Vorabelle</div>
  <div class="tagline front">Where Calm Finds Bloom</div>
  <div class="product-name front">Gentle<br>Exfoliating Herbs</div>

  <section class="panel-text skin-types">All Skin Types<br>Particularly beneficial for Sensitive,<br>stressed and delicate skins</section>
  <div class="badge-label" style="left:619px; top:363px;">Australian<br>Made</div>
  <div class="badge-label" style="left:653px; top:363px;">100%<br>Vegan</div>
  <div class="badge-label" style="left:684px; top:363px;">Cruelty<br>Free</div>
  <div class="badge-label" style="left:637px; top:408px;">Please<br>Recycle</div>
  <div class="badge-label" style="left:666px; top:408px;">6 months<br>once open</div>
  <section class="panel-text care-note">Store in a cool dry place Caution For external use only. Avoid contact with eyes. If irritation occurs, discontinue use.</section>
  <div class="panel-text web-address">www.vorabelle.com</div>

  <div class="bloom alt" role="img" aria-label="Photograph of a white jasmine flower with green leaves"></div>
  <div class="brand-name alt">Vorabelle</div>
  <div class="tagline alt">Where Calm Finds Bloom</div>
  <div class="product-name alt">Gentle<br>Exfoliating Herbs</div>
</main>
</body>
</html>
```